Business Card Design

We have our logo and everything in place. Looking to have a layout for our new business cards designed. These will be printed with a matte finish, possibly rounded corners, and looking to incorporate some cool spot UV layers into the design.

Ive uploaded the existing card front and back as well as our logo.

Card Size Will Be 3.5" x 2"

```html
<!DOCTYPE html>
<html lang="en">
<head>
<meta charset="utf-8">
<title>Summit Deck and Rail – Business Cards</title>
<link href="https://fonts.googleapis.com/css2?family=PT+Sans:ital,wght@0,400;1,400&display=swap" rel="stylesheet">
<style>
  :root {
    --backdrop: #0f2332;
    --card-front: #0a0a0a;
    --card-back: #1fb3d4;
    --ink-light: #ffffff;
    --ink-soft: #cfcfcf;
    --rule: #8a8a8a;
    --spot-uv: #5fd3ee;
  }
  * { margin: 0; padding: 0; box-sizing: border-box; }
  html, body {
    width: 1200px; height: 1099px; overflow: hidden;
    background: var(--backdrop);
    font-family: "PT Sans", sans-serif;
  }
  .canvas {
    position: relative; width: 1200px; height: 1099px;
  }
  .card {
    position: absolute; left: 200px; width: 800px; height: 457px;
    border-radius: 6px;
    overflow: hidden;
  }
  .card--front { top: 62px; background: var(--card-front); color: var(--ink-light); }
  .card--back { top: 580px; background: var(--card-back); }

  .brand {
    position: absolute; right: 70px; top: 70px;
    text-align: center;
  }
  .brand__name {
    font-size: 44px; font-weight: 400; color: var(--ink-light);
    letter-spacing: 0.5px; line-height: 1;
  }
  .holder {
    position: absolute; left: 56px; top: 185px; right: 56px;
  }
  .holder__name { font-size: 30px; line-height: 1.1; }
  .holder__title-row { display: flex; align-items: center; gap: 12px; margin-top: 6px; }
  .holder__title { font-style: italic; font-size: 19px; color: var(--ink-soft); }
  .holder__rule { flex: 1; height: 1px; background: var(--rule); }

  .contacts {
    position: absolute; right: 40px; top: 315px;
    list-style: none; text-align: right;
  }
  .contacts__item {
    display: flex; justify-content: flex-end; align-items: center; gap: 12px;
    font-size: 22px; line-height: 36px;
  }
  .contacts__icon { width: 22px; height: 22px; flex: none; }

  .brand--spot {
    position: absolute; left: 0; right: 0; top: 190px; text-align: center;
  }
  .brand--spot .brand__name { color: var(--spot-uv); font-size: 76px; }
</style>
</head>
<body>
<div class="canvas">
  <section class="card card--front">
    <div class="brand">
      <p class="brand__name">Summit Deck &amp; Rail</p>
    </div>
    <div class="holder">
      <p class="holder__name">Daniel Mercer</p>
      <div class="holder__title-row">
        <span class="holder__title">President</span>
        <span class="holder__rule"></span>
      </div>
    </div>
    <ul class="contacts">
      <li class="contacts__item">403.555.0187
        <svg class="contacts__icon" viewBox="0 0 24 24" aria-hidden="true">
          <path fill="#fff" d="M4 9c0-3 4-4 8-4s8 1 8 4v2h-4V9H8v2H4z"/>
          <rect x="5" y="12" width="14" height="8" rx="1.5" fill="#fff"/>
          <circle cx="12" cy="16" r="2" fill="#0a0a0a"/>
        </svg>
      </li>
      <li class="contacts__item">www.summitdeckandrail.com
        <svg class="contacts__icon" viewBox="0 0 24 24" aria-hidden="true">
          <circle cx="12" cy="12" r="10" fill="#fff"/>
          <circle cx="12" cy="12" r="6" fill="none" stroke="#0a0a0a" stroke-width="1.5"/>
          <path d="M6 12h12M12 6v12" stroke="#0a0a0a" stroke-width="1.5"/>
        </svg>
      </li>
      <li class="contacts__item">summitdeckandrail@gmail.com
        <svg class="contacts__icon" viewBox="0 0 24 24" aria-hidden="true">
          <circle cx="12" cy="12" r="10" fill="#fff"/>
          <rect x="6" y="8" width="12" height="8" fill="#0a0a0a"/>
          <path d="M6 8l6 5 6-5" fill="none" stroke="#fff" stroke-width="1.2"/>
        </svg>
      </li>
    </ul>
  </section>

  <section class="card card--back">
    <div class="brand brand--spot">
      <p class="brand__name">Summit Deck &amp; Rail</p>
    </div>
  </section>
</div>
</body>
</html>
```